Los Fogones Ember Poultry MENU!

We are looking for a simple, rustic and modern menu that highlights our passion for healthy and tasty chickens!
We want to highlight our menu but yet keep it very simple.

Attached is info on our logo and our menu information

Target Market(s)

We want to attract all customers but primarily we want to focus on the following 3 markets: Healthy concerned, Food fanatics and Family based.

Industry/Entity Type

Fast Food Restaurant

Requirements
Must have
• We must have our logo on the flyer,
• rustic yet modern
• you must use our colors on the flyer and
• KEEP IT SIMPLE
• Here is our Menu below
• Attached is our final menu we are going to advertise:
• Chicken:
• 1/4 Chicken Dark $6.99
• 1/4 Chicken White $7.99
• 1/2 Chicken white + dark $9.99
• 1/2 chicken all white $10.99
• All come with choice of 2 small sides
• 1 whole chicken family meal ( served with 3 Large sides + 2 liter soda) $23.99
• 2 whole chicken family meal (served with 4 Large sides + 2 liter soda) $33.99
• Extra whole chicken (Chicken only) $13.99
• Sides available with meals:
• - Cilantro infused white rice
• - Hand Cut Fries
• - Hand Cut Sweet potato Fries
• - Yucca
• - Fried Plantains
• - Pinto Beans
• - Black Beans
• - Steamed vegetable medley
• - Cesar Salad
• - Garden Salad
• - House Salad
• - Tortillas
• (reg side: $1.99) Large Side $3.29
• Other Dishes available:
• Lomo Saltado: $12.99
• Pesto Pasta (Tallarin Verde) w/ Steak or 1/4 chicken $ 12.99
• Bistek a lo Pobre: $12.99
• Marcos Treat $12.99 (Chicken filet grilled) w/ salads
• Tallarin Saltado (Garden style pasta) w/ Chicken $11.99, Steak add. $1.49
• Tallarin a la Huancaina $12.99 w/ steak or 1/4 chicken
• Garden Salad ($6.99) Add chicken or steak $1.99
• Cesar Salad ($6.99) Add Chicken or steak $1.99
• House Salad ($6.99) Add chicken or steak $1.99
• DRINKS/DESSERTS:
• - SODAS: REG. $1.99 LARGE 2.59
• - ANDA FIZZ: $1.69 CAN; $1.99 IMPORTED; $2.59 BOTTLE
• - SPECIALTY DRINKS: $2.59
• - ALFAJOR $2.99
• - PERUVIAN FLAN $4.99
• - 3 LECHES $4.99
• (SAVE $1.00 OF ANY DESSERT WITH PURCHASE OF MEAL)
Nice to have
• We would love to see it all in 1 half sheet
Should not have
• can not have too much on it where its confusing.

```html
<!DOCTYPE html>
<html lang="en">
<head>
<meta charset="utf-8">
<title>Los Fogones Ember Poultry – Menu</title>
<link rel="stylesheet" href="https://fonts.googleapis.com/css2?family=Josefin+Sans:wght@300;400;600;700&family=Montserrat:wght@700&display=swap">
<style>
  :root{
    --bg:#2b2d31;
    --red:#e0201f;
    --orange:#f07b2a;
    --green:#8fe05a;
    --text:#f2f2f2;
    --muted:#d6d6d6;
  }
  *{margin:0;padding:0;box-sizing:border-box}
  html,body{width:927px;height:1200px;overflow:hidden;background:var(--bg)}
  .menu{position:relative;width:927px;height:1200px;background:var(--bg);color:var(--text);
    font-family:"Josefin Sans",sans-serif;overflow:hidden}
  .stripe{position:absolute;left:0;width:100%}
  .stripe--top{top:0;height:30px;
    background:repeating-linear-gradient(135deg,var(--red) 0 14px,var(--bg) 14px 24px)}
  .stripe--bottom{bottom:0;height:36px;
    background:repeating-linear-gradient(135deg,var(--orange) 0 14px,var(--bg) 14px 24px)}

  .brand{position:absolute;top:128px;left:0;width:100%;text-align:center;color:var(--red);
    font-family:"Josefin Sans",sans-serif;font-weight:400}
  .brand__name{font-size:52px;letter-spacing:6px;line-height:1}
  .brand__tag{font-size:24px;letter-spacing:1px;margin-top:10px;padding-left:200px}
  .brand__dot{display:inline-block;width:14px;height:14px;border-radius:50%;background:var(--red);
    vertical-align:middle;margin:0 14px 8px}

  .section-title{position:absolute;border:3px solid var(--red);height:70px;display:flex;align-items:center;
    font-family:"Montserrat",sans-serif;font-weight:700;font-size:26px;letter-spacing:7px;color:var(--green)}
  .section-title--chicken{left:42px;top:254px;width:592px;padding-left:37px}
  .section-title--salad{left:645px;top:254px;width:231px;padding-left:30px}
  .section-title--sides{left:42px;top:709px;width:363px;padding-left:50px}
  .section-title--other{left:416px;top:709px;width:452px;padding-left:82px}

  .item{position:absolute;font-size:18px;letter-spacing:2.2px;line-height:26px;text-transform:uppercase}
  .item__row{display:flex}
  .item__name{width:157px}
  .item__note{text-transform:none;font-size:15px;letter-spacing:.8px;font-weight:300;color:var(--muted);line-height:23px}
  .chicken-col1 .item{left:42px}
  .item--wide .item__name{width:228px}

  .salad-item{position:absolute;right:46px;text-align:right;font-size:18px;letter-spacing:2.2px}
  .salad-item__add{font-size:15px;letter-spacing:.8px;font-weight:300;color:var(--muted);margin-top:14px;margin-right:6px}

  .sides-list{position:absolute;left:42px;top:800px;list-style:none;font-size:17px;letter-spacing:.8px;
    font-weight:300;line-height:29.5px;color:var(--muted)}
  .side-price{position:absolute;right:532px;text-align:right;font-size:15px;letter-spacing:.5px;font-weight:300;
    line-height:25px;color:var(--muted)}

  .dish{position:absolute;left:423px;width:438px;font-size:18px;letter-spacing:2.2px;text-transform:uppercase}
  .dish__price{position:absolute;right:0;top:0;font-size:16px;letter-spacing:.5px;color:var(--muted);font-weight:300}
  .dish__note{text-transform:none;font-size:15px;letter-spacing:.8px;font-weight:300;color:var(--muted);
    line-height:24px;padding-left:12px}
</style>
</head>
<body>
<div class="menu">
  <div class="stripe stripe--top"></div>

  <header class="brand">
    <div class="brand__name">LOS<span class="brand__dot"></span>FOGONES</div>
    <div class="brand__tag">ember poultry</div>
  </header>

  <h2 class="section-title section-title--chicken">CHICKEN</h2>
  <h2 class="section-title section-title--salad">SALAD</h2>

  <div class="chicken-col1">
    <div class="item" style="top:355px"><div class="item__row"><span class="item__name">1/4 Chicken</span><span>| $6.99</span></div>Dark</div>
    <div class="item" style="top:413px"><div class="item__row"><span class="item__name">1/4 Chicken</span><span>| $6.99</span></div>White</div>
    <div class="item" style="top:480px"><div class="item__row"><span class="item__name">1/2 Chicken</span><span>| $6.99</span></div>White + Dark</div>
    <div class="item" style="top:553px;left:45px"><div class="item__row"><span class="item__name" style="width:149px">1/2 Chicken</span><span>| $10.99</span></div>All White</div>
    <div class="item item__note" style="top:625px;width:230px">*All come with choice of 2 small sides,</div>
  </div>

  <div class="item item--wide" style="top:350px;left:307px"><div class="item__row"><span class="item__name" style="width:205px">1 Whole Chicken</span><span>| $23.99</span></div>Family Meal
    <div class="item__note" style="margin-top:4px;width:290px">Served with 3 Large sides + 2 liter soda</div></div>
  <div class="item item--wide" style="top:467px;left:307px"><div class="item__row"><span class="item__name">2 Whole Chickens</span><span>| $33.99</span></div>Family Meal
    <div class="item__note" style="margin-top:4px;width:300px">Served with 4 Large + 2 liter soda</div></div>
  <div class="item item--wide" style="top:580px;left:307px"><div class="item__row"><span class="item__name">Extra Whole</span><span>| $13.99</span></div>Chicken</div>

  <div class="salad-item" style="top:356px">GARDEN SALAD | $6.99<div class="salad-item__add">Add chicken or steak $1.99</div></div>
  <div class="salad-item" style="top:449px">CESAR SALAD | $6.99<div class="salad-item__add" style="margin-top:10px">Add chicken or steak $1.99</div></div>
  <div class="salad-item" style="top:543px">HOUSE SALAD | $6.99<div class="salad-item__add" style="margin-top:14px">Add chicken or steak $1.99</div></div>

  <h2 class="section-title section-title--sides">SIDE DISHES</h2>
  <h2 class="section-title section-title--other">OTHER DISHES</h2>

  <ul class="sides-list">
    <li>Cilantro infused white rice</li>
    <li>Hand Cut Fries</li>
    <li>Hand Cut Sweet potato Fries</li>
    <li>Yucca</li>
    <li>Fried Plantains</li>
    <li>Pinto Beans</li>
    <li>Black Beans</li>
    <li>Steamed vegetable medley</li>
    <li>Cesar Salad</li>
    <li>Garden Salad</li>
    <li>House Salad</li>
    <li>Tortillas</li>
  </ul>
  <div class="side-price" style="top:805px">Regular&nbsp;&nbsp;Side<br>$1.99</div>
  <div class="side-price" style="top:886px">Large Side<br>$3.29</div>

  <div class="dish" style="top:803px">Lomo Saltado<span class="dish__price" style="top:6px">$12.99</span></div>
  <div class="dish" style="top:850px">Pesto Pasta(Tallarin Verde)<span class="dish__price" style="top:4px">$12.99</span>
    <div class="dish__note">with Steak or 1/4 chicken</div></div>
  <div class="dish" style="top:908px">Bistek a lo Pobre<span class="dish__price" style="top:-6px">$12.99</span></div>
  <div class="dish" style="top:952px">Marcos Treat<span class="dish__price" style="top:-12px">$12.99</span>
    <div class="dish__note">Chicken filet grilled with salad</div></div>
  <div class="dish" style="top:1016px">Tallarin Saltado<span class="dish__price" style="top:0;right:4px">$11.99</span>
    <div class="dish__note">Grades Style Pasta with Chicken<br>Steak add. $1.49</div></div>
  <div class="dish" style="top:1099px">Tallarin a la Huancaina<span class="dish__price">$12.99</span>
    <div class="dish__note">with Steak or 1/4 Chicken</div></div>

  <div class="stripe stripe--bottom"></div>
</div>
</body>
</html>
```